Redesign Colorful Business Card

Please redesign the card attached. It is too busy. Please don't eliminate any of the words. The repetivite word "free" can be used less often.

Target Market(s)

College Students.

Contact Information for Business Card

The details listed in the attached image

Font styles to use
Sans Serif

Requirements
Must have
• A clear and simple presentation and must be attractive.

```html
<!DOCTYPE html>
<html lang="en">
<head>
<meta charset="UTF-8">
<title>StudyLeap Business Card</title>
<link href="https://fonts.googleapis.com/css2?family=Roboto+Condensed:wght@700&family=Open+Sans:wght@400&display=swap" rel="stylesheet">
<style>
  :root {
    --backdrop: #4b4b4b;
    --crimson: #c11d33;
    --red: #e8393a;
    --orange: #f5871f;
    --amber: #fbb316;
    --yellow: #fcd80f;
    --green: #7cc243;
    --box-red: #d42028;
    --box-orange: #f06a23;
    --box-yellow: #fdd531;
    --band-blue: #3e55a5;
    --ink: #111111;
    --white: #ffffff;
    --free-red: #e0352b;
  }
  * { margin: 0; padding: 0; box-sizing: border-box; }
  html, body {
    width: 1200px;
    height: 960px;
    overflow: hidden;
    background: var(--backdrop);
  }
  .card {
    position: absolute;
    left: 180px;
    top: 240px;
    width: 840px;
    height: 480px;
    overflow: hidden;
    background: linear-gradient(112deg,
      var(--crimson) 0%, var(--red) 28%, var(--orange) 52%,
      var(--amber) 66%, var(--yellow) 78%, var(--green) 100%);
    font-family: "Roboto Condensed", "Arial Narrow", sans-serif;
  }
  .mascot {
    position: absolute;
    left: 74px;
    top: 52px;
    width: 244px;
    height: 278px;
    border-radius: 46% 40% 18% 18%;
    background: linear-gradient(135deg, #4f7cc4 0%, #f08080 40%, #e8262d 70%, #f7c531 100%);
  }
  .site-name {
    position: absolute;
    left: 52px;
    top: 330px;
    font-size: 46px;
    line-height: 1;
    color: var(--ink);
    font-weight: 700;
    letter-spacing: -0.5px;
  }
  .offer-frame {
    position: absolute;
    left: 354px;
    top: 94px;
    width: 90px;
    height: 274px;
    border: 6px solid var(--ink);
    border-right: none;
  }
  .offer-word {
    position: absolute;
    left: 372px;
    top: 160px;
    width: 54px;
    height: 148px;
    display: flex;
    align-items: center;
    justify-content: center;
  }
  .offer-word span {
    display: block;
    transform: rotate(-90deg);
    font-size: 62px;
    line-height: 1;
    letter-spacing: 2px;
    color: var(--free-red);
    white-space: nowrap;
  }
  .benefit {
    position: absolute;
    left: 434px;
    width: 406px;
    height: 100px;
    display: flex;
    flex-direction: column;
    justify-content: center;
    font-size: 29px;
    line-height: 1.25;
    text-transform: uppercase;
  }
  .benefit--time { top: 56px; background: var(--box-red); color: var(--white); padding-left: 24px; }
  .benefit--class { top: 178px; background: var(--box-orange); color: var(--white); padding-left: 18px; }
  .benefit--memory { top: 301px; background: var(--box-yellow); color: var(--ink); padding-left: 28px; }
  .copyright-band {
    position: absolute;
    left: 0;
    top: 426px;
    width: 840px;
    height: 30px;
    background: var(--band-blue);
    color: var(--white);
    font-family: "Open Sans", Arial, sans-serif;
    font-size: 19px;
    line-height: 30px;
    text-align: center;
  }
</style>
</head>
<body>
  <main class="card">
    <div class="mascot" role="img" aria-label="Colourful geometric elephant mascot illustration"></div>
    <div class="site-name">StudyLeap.com</div>

    <div class="offer-frame"></div>
    <div class="offer-word"><span>FREE</span></div>

    <div class="benefit benefit--time">
      <p>Cut study time</p>
      <p>town by up to 50%</p>
    </div>
    <div class="benefit benefit--class">
      <p>Learn a subject without</p>
      <p>having to go to class</p>
    </div>
    <div class="benefit benefit--memory">
      <p>Memorize anything</p>
      <p>quickly</p>
    </div>

    <div class="copyright-band">Copyright StudyLeap Services, LLC 2013-2022 All Rights Reserved</div>
  </main>
</body>
</html>
```